Webdesign für Beratung von Firmen zum Thema Radon
Zielgruppe
Firmenname: Lumivelde - Ich informiere und berate als Radon Fachperson, Privatpersonen sowie Firmen zum Thema Radon, und die Gefahren die damit verbunden sind in bestehenden Gebäuden und Neubauten. Die Leistung erfolgt in Form eines ausgearbeiteten Sanierungskonzeptes bzw. bautechnische Maßnahmen beim Neubau.
Aufgabenstellung
Keep it simple and clean, weniger ist mehr. Die beigefügten Info-Grafiken sollen nur als Information dienen zum Thema Radon, und sollen nicht verwendet werden - ich hoffe hier doch besseres Bildmaterial von euch zu bekommen :-)

```html
<!DOCTYPE html>
<html lang="de">
<head>
<meta charset="utf-8">
<title>Lumivelde – Radon Beratung</title>
<link href="https://fonts.googleapis.com/css2?family=Poppins:wght@300;400;500;600;700&display=swap" rel="stylesheet">
<style>
:root{
  --green:#35a047;
  --teal:#1f8478;
  --blue-deep:#1b6dbb;
  --blue-footer:#1a6ab6;
  --ink:#3e4a52;
  --text:#6b7378;
  --light-green:#effaf0;
  --light-blue:#eaf4fd;
  --grey-bg:#f3f3f3;
  --grey-block:#c6c7c8;
  --white:#ffffff;
}
*{box-sizing:border-box;margin:0;padding:0}
html,body{width:1200px;height:5172px;overflow:hidden}
body{font-family:'Poppins',sans-serif;color:var(--text);background:var(--white);position:relative}
p{font-size:13px;line-height:22px;font-weight:300}
h2.section-title{position:absolute;left:0;width:1200px;text-align:center;color:var(--green);font-size:27px;font-weight:600}
h2.section-title::after{content:"";display:block;width:58px;height:2px;background:var(--green);margin:8px auto 0}
.centered-text{position:absolute;left:190px;width:820px;text-align:center}

.site-header{position:absolute;top:0;left:0;width:1200px;height:68px;background:var(--white);border-top:3px solid var(--green);z-index:3}
.nav a{position:absolute;top:24px;font-size:13px;color:var(--ink);text-decoration:none}
.logo-badge{position:absolute;left:520px;top:0;width:160px;height:130px;z-index:4}
.logo-name{position:absolute;left:0;top:74px;width:160px;text-align:center;font-size:15px;font-weight:600;color:var(--ink);letter-spacing:1px}
.logo-dot{position:absolute;left:68px;top:28px;width:24px;height:24px;border-radius:50%;background:var(--green)}
.call-btn{position:absolute;left:922px;top:12px;width:160px;height:40px;background:var(--teal);border-radius:4px;color:var(--white);text-align:center;font-size:12px;font-weight:600;line-height:15px;padding-top:5px}
.call-btn small{display:block;font-size:10px;font-weight:400}

.hero{position:absolute;top:68px;left:0;width:1200px;height:490px;background:linear-gradient(100deg,#3aa55a 0%,#47a38a 45%,#3f8bc7 75%,#3b82c6 100%)}
.hero h1{position:absolute;left:170px;top:152px;font-size:35px;font-weight:600;color:var(--white);letter-spacing:1px}
.hero p{position:absolute;left:170px;top:220px;width:470px;color:var(--white);font-size:12px}
.hero .outline-btn{position:absolute;left:170px;top:322px;width:156px;height:38px;border:1.5px solid var(--white);border-radius:4px;color:var(--white);text-align:center;line-height:35px;font-size:15px;font-weight:300}
.hero-graphic{position:absolute;left:730px;top:130px;width:322px;height:322px;border-radius:18px;background:linear-gradient(160deg,#2f6fa8,#24537f)}

.team-left{position:absolute;top:738px;left:0;width:600px;height:598px;background:var(--light-green)}
.team-right{position:absolute;top:738px;left:600px;width:600px;height:598px;background:var(--light-blue)}
.frame{position:absolute;border:2px solid var(--teal)}
.photo{position:absolute}
.member h3{position:absolute;font-size:23px;font-weight:600;color:var(--ink)}
.member p{position:absolute;width:340px;font-size:12px}
.green-btn{position:absolute;width:158px;height:38px;border-radius:4px;background:linear-gradient(90deg,var(--green),var(--teal));color:var(--white);font-size:12px;text-align:center;line-height:38px}

.row-title{position:absolute;font-size:16px;font-weight:600;color:var(--ink)}
.row-text{position:absolute;width:448px;font-size:12.5px;line-height:21.5px}

.cta{position:absolute;top:2596px;left:0;width:1200px;height:204px;background:linear-gradient(90deg,#35a047,#2a8d78);text-align:center;color:var(--white)}
.cta h2{margin-top:38px;font-size:21px;font-weight:600;line-height:36px}
.cta .outline-btn{position:absolute;left:506px;top:132px;width:186px;height:38px;border:1.5px solid var(--white);border-radius:4px;line-height:35px;font-size:15px;font-weight:300}

.services{position:absolute;top:2800px;left:0;width:1200px;height:996px;background:var(--grey-bg)}
.grey-block{position:absolute;background:var(--grey-block)}
.service-card{position:absolute;background:var(--white);padding:8px}
.service-card .photo{position:relative;width:100%;height:100%}
.big-num{position:absolute;font-size:170px;font-weight:700;color:var(--white);line-height:1}
.service h2{position:absolute;font-size:27px;font-weight:600;color:var(--green)}
.service h2::after{content:"";display:block;width:58px;height:2px;background:var(--green);margin-top:6px}
.service h3{position:absolute;font-size:19px;font-weight:600;color:var(--ink)}
.service p{position:absolute;width:380px;font-size:12.5px}
.service h4{position:absolute;font-size:12.5px;font-weight:600;color:var(--ink)}
.service ul{position:absolute;list-style:none;font-size:12.5px;font-weight:300;line-height:21.5px}
.service li::before{content:"";display:inline-block;width:6px;height:6px;background:var(--blue-deep);margin-right:10px;vertical-align:middle}

.ref-card{position:absolute;top:4086px;width:268px}
.ref-card .photo{position:relative;height:164px;border-bottom:3px solid var(--green)}
.ref-card h3{margin:16px 20px 10px;font-size:20px;font-weight:600;color:var(--ink)}
.ref-card p{margin:0 20px;font-size:12.5px}
.ref-card.faded{opacity:.3}
.arrow-btn{position:absolute;top:4410px;width:40px;height:38px;border:1.5px solid #b8c0c6;border-radius:3px;background:var(--white)}
.arrow-btn.active{border-color:var(--blue-deep)}

.contact{position:absolute;top:4500px;left:0;width:1200px;height:510px;background:#f4f5f6}
.contact h2{position:absolute;left:192px;top:96px;font-size:29px;font-weight:600;color:var(--blue-deep)}
.contact .intro{position:absolute;left:192px;top:142px;width:360px;font-size:12.5px}
.info{position:absolute;left:198px;border-left:3px solid var(--blue-deep);padding-left:20px;height:50px}
.info b{display:block;font-size:12.5px;font-weight:600;color:var(--ink)}
.info span{display:block;margin-top:6px;font-size:12.5px;font-weight:300}
.field{position:absolute;left:616px;width:428px;background:var(--white);border:1px solid #e5e7e9;font-size:12px;font-style:italic;color:#a6adb2;padding:20px}
.submit{position:absolute;left:616px;top:4886px;width:428px;height:68px;background:var(--blue-deep);border-radius:3px;color:var(--white);text-align:center;line-height:68px;font-size:15px;font-weight:600;letter-spacing:10px}

.site-footer{position:absolute;top:5010px;left:0;width:1200px;height:162px;background:var(--blue-footer);color:var(--white)}
.site-footer .links a{position:absolute;top:50px;font-size:13px;color:var(--white);text-decoration:none}
.site-footer .go{position:absolute;left:726px;top:48px;font-size:17px}
.site-footer .go-btn{position:absolute;left:844px;top:40px;width:132px;height:42px;background:#2d8ae6;border-radius:4px;font-size:11px;text-align:center;line-height:42px}
.copyright{position:absolute;top:114px;left:0;width:1200px;height:48px;background:#1760a8;text-align:center;font-size:10px;line-height:48px;font-weight:300}
</style>
</head>
<body>

<header class="site-header">
  <nav class="nav">
    <a style="left:170px">Über uns</a>
    <a style="left:270px">Was ist Radon?</a>
    <a style="left:410px">Leistung</a>
    <a style="left:716px">Referenzen</a>
    <a style="left:832px">Kontakt</a>
  </nav>
  <div class="call-btn">(555) 214-7730<small>Jetzt Anrufen</small></div>
</header>
<div class="logo-badge">
  <svg width="160" height="130" style="position:absolute;left:0;top:0"><polygon points="0,0 160,0 160,104 80,130 0,104" fill="#fff"/></svg>
  <div class="logo-dot"></div>
  <div class="logo-name">LUMIVELDE</div>
</div>

<section class="hero">
  <h1>IONISING RADIATION</h1>
  <p>Nulla Lorem mollit cupidatat irure. Laborum magna nulla duis ullamco cillum dolor. Voluptate exercitation incididunt aliquip deserunt reprehenderit elit laborum.</p>
  <div class="outline-btn">Mehr Infos</div>
  <div class="hero-graphic" role="img" aria-label="Grafik eines Periodensystem-Felds für das Element Radon"></div>
</section>

<h2 class="section-title" style="top:598px">Über uns</h2>
<p class="centered-text" style="top:658px">Radon ist ein sehr bewegliches, radioaktives Edelgas, das man weder sehen, riechen oder schmecken kann. Es entsteht beim radioaktiven Zerfall von Uran. Uran kom</p>

<section class="team-left"></section>
<section class="team-right"></section>
<div class="member">
  <div class="frame" style="left:190px;top:806px;width:378px;height:274px"></div>
  <div class="photo" role="img" aria-label="Porträtfoto von Mara Lindqvist" style="left:168px;top:794px;width:380px;height:272px;background:linear-gradient(135deg,#8a7b6a,#cfc8bb 60%,#e8e4dc)"></div>
  <h3 style="left:186px;top:1104px">Mara Lindqvist</h3>
  <p style="left:184px;top:1150px">Amet minim mollit non deserunt ullamco est sit aliqua dolor do amet sint. Velit officia consequat duis enim velit mollit. Exercitation veniam consequat sunt nostrud amet.</p>
  <div class="green-btn" style="left:184px;top:1262px">Read More</div>
</div>
<div class="member">
  <div class="frame" style="left:640px;top:806px;width:378px;height:274px"></div>
  <div class="photo" role="img" aria-label="Porträtfoto von Jonas Berger" style="left:658px;top:794px;width:380px;height:272px;background:linear-gradient(135deg,#6e4a36,#b88f72 50%,#4d5f6a)"></div>
  <h3 style="left:676px;top:1104px">Jonas Berger</h3>
  <p style="left:674px;top:1150px">Amet minim mollit non deserunt ullamco est sit aliqua dolor do amet sint. Velit officia consequat duis enim velit mollit. Exercitation veniam consequat sunt nostrud amet.</p>
  <div class="green-btn" style="left:674px;top:1262px">Read More</div>
</div>

<h2 class="section-title" style="top:1388px">Radon</h2>
<p class="centered-text" style="top:1448px">Radon ist ein sehr bewegliches, radioaktives Edelgas, das man weder sehen, riechen oder schmecken kann. Es entsteht beim radioaktiven Zerfall von Uran. Uran kommt zum Beispiel im Erdboden oder in Baumaterialien vor.</p>

<div class="frame" style="left:292px;top:1558px;width:296px;height:264px"></div>
<div class="photo" role="img" aria-label="Gelbes Warnschild mit Radioaktivitätssymbol und Aufschrift Radon Gas" style="left:226px;top:1568px;width:290px;height:250px;background:linear-gradient(160deg,#f6cf1a,#e0b20c)"></div>
<h3 class="row-title" style="left:622px;top:1576px">Was ist Radon?</h3>
<p class="row-text" style="left:622px;top:1604px">Aus natürlichem Uran in Böden und Gesteinen entsteht Radon, das sich in Gebäuden ansammeln kann und dort das Lungenkrebsrisiko der Bewohner erhöht. Radon ist ein sehr bewegliches, radioaktives Edelgas, das überall in der Umwelt vorkommt. Bei seinem Zerfall sendet es Strahlung aus. Radon ist nach dem Rauchen eine der wichtigsten Ursachen für Lungenkrebs. Etwa fünf Prozent der Todesfälle durch Lungenkrebs in der Bevölkerung sind nach aktuellen Erkenntnissen auf Radon und seine Zerfallsprodukte in Gebäuden zurückzuführen.</p>

<h3 class="row-title" style="left:138px;width:448px;text-align:right;top:1934px">Wo kommt Radon vor?</h3>
<p class="row-text" style="left:138px;top:1962px;text-align:right">Radon kommt in unterschiedlichen Konzentrationen überall in unserer Umwelt vor. Aus dem Untergrund von Gebäuden gelangt Radon auch in die Innenräume von Häusern, wo es sich anreichern kann. Insbesondere bei seltenem Lüften kann dies zu hohen Radon-Konzentrationen führen, die gesundheitsgefährdend sind. Die Radon-Konzentrationen im Boden, in der Luft und in Innenräumen sind lokal und regional unterschiedlich.</p>
<div class="frame" style="left:622px;top:1894px;width:294px;height:256px"></div>
<div class="photo" role="img" aria-label="Illustration eines Hauses mit grünen Pfeilen für aufsteigendes Radongas" style="left:660px;top:1940px;width:402px;height:210px;background:linear-gradient(180deg,#f7f7f7,#b8b8b6 60%,#8fa88a)"></div>

<div class="frame" style="left:292px;top:2232px;width:296px;height:260px"></div>
<div class="photo" role="img" aria-label="Foto eines Wohnhauses mit Vorgarten" style="left:202px;top:2288px;width:348px;height:216px;background:linear-gradient(180deg,#c8d0c6,#8a9170 55%,#3f6b34)"></div>
<h3 class="row-title" style="left:622px;top:2270px">Wie kann ich mich vor Radon schützen?</h3>
<p class="row-text" style="left:622px;top:2298px">Ist zu viel Radon im Haus, hilft es als Erstmaßnahme, regelmäßig und intensiv zu lüften. Da hohe Radon-Konzentrationen in der Regel dadurch entstehen, dass aus dem Baugrund radonhaltige Bodenluft eindringt, sollten neue Gebäude durchgehend gegen Bodenfeuchte und damit auch gegen das Eindringen von Radon abgedichtet und undichte Stellen in Bestandsgebäuden identifiziert und beseitigt werden.</p>

<section class="cta">
  <h2>Kostenlose Kostenvoranschläge und Beratungsgespräche<br>(555) 214-7730</h2>
  <div class="outline-btn">Jetzt Anrufen</div>
</section>

<section class="services"></section>
<div class="service">
  <div class="grey-block" style="left:222px;top:2872px;width:320px;height:446px"></div>
  <div class="service-card" style="left:168px;top:2908px;width:336px;height:458px">
    <div class="photo" role="img" aria-label="Foto zweier Bauexperten mit Helm bei der Besprechung" style="background:linear-gradient(135deg,#e9e4dc,#8d7a63 45%,#4a3d32)"></div>
  </div>
  <div class="big-num" style="left:352px;top:2904px">1.</div>
  <h2 style="left:576px;top:2860px">Leistung</h2>
  <h3 style="left:576px;top:2992px">Begutachtung und Beratung</h3>
  <p style="left:576px;top:3032px">Amet minim mollit non deserunt ullamco est sit aliqua dolor do amet sint. Velit officia consequat duis enim velit mollit. Exercitation veniam consequat sunt nostrud amet.</p>
  <h4 style="left:576px;top:3114px">Fachwissen</h4>
  <ul style="left:576px;top:3146px"><li>Cras ornare tristique elit.</li><li>Vivamus vestibulum ntulla nec ante.</li><li>Praesent placerat risus quis eros.</li><li>Fusce pellentesque suscipit nibh.</li><li>Integer vitae libero ac risus egestas placerat.</li></ul>
</div>
<div class="service">
  <div class="grey-block" style="left:756px;top:3370px;width:260px;height:444px"></div>
  <div class="service-card" style="left:644px;top:3402px;width:336px;height:454px">
    <div class="photo" role="img" aria-label="Foto einer Hausfassade mit Radon-Abluftrohr" style="background:linear-gradient(180deg,#3f86c8,#7a8fa0 30%,#525a60)"></div>
  </div>
  <div class="big-num" style="left:664px;top:3400px">2.</div>
  <h3 style="left:178px;top:3466px">Sanierung</h3>
  <p style="left:178px;top:3506px">Amet minim mollit non deserunt ullamco est sit aliqua dolor do amet sint. Velit officia consequat duis enim velit mollit. Exercitation veniam consequat sunt nostrud amet.</p>
  <h4 style="left:178px;top:3588px">Fachwissen</h4>
  <ul style="left:178px;top:3618px"><li>Cras ornare tristique elit.</li><li>Vivamus vestibulum ntulla nec ante.</li><li>Praesent placerat risus quis eros.</li><li>Fusce pellentesque suscipit nibh.</li><li>Integer vitae libero ac risus egestas placerat.</li></ul>
</div>

<h2 class="section-title" style="top:3922px">Referenzen</h2>
<p class="centered-text" style="left:210px;width:780px;top:3978px">Aliqua id fugiat nostrud irure ex duis ea quis id quis ad et. Sunt qui esse pariatur duis deserunt mollit dolore cillum minim tempor enim. Elit aute irure tempor cupidatat incididunt sint deserunt ut voluptate aute id nostrud nisi.</p>

<div class="ref-card faded" style="left:-146px"><div class="photo" role="img" aria-label="Foto eines hellen Wohnraums" style="background:linear-gradient(135deg,#e8e6e2,#c9bfb3)"></div><h3>Arvenhof</h3><p>Amet minim mollit non deserunt ullamco est sit aliqua dolor do amet sint.</p></div>
<div class="ref-card" style="left:160px"><div class="photo" role="img" aria-label="Foto eines Essbereichs mit Küche" style="background:linear-gradient(135deg,#eceae6,#b9a996 55%,#6d6257)"></div><h3>Velmora</h3><p>Amet minim mollit non deserunt ullamco est sit aliqua dolor do amet sint.</p></div>
<div class="ref-card" style="left:466px"><div class="photo" role="img" aria-label="Foto eines Schlafzimmers mit dunkler Wand" style="background:linear-gradient(90deg,#f1f0ed,#3a3f44 55%,#d9d6d0)"></div><h3>Brightwell</h3><p>Amet minim mollit non deserunt ullamco est sit aliqua dolor do amet sint.</p></div>
<div class="ref-card" style="left:772px"><div class="photo" role="img" aria-label="Foto eines Wohnzimmers mit blauem Sofa" style="background:linear-gradient(135deg,#efece7,#b69b84 55%,#4e6f8c)"></div><h3>Corvane</h3><p>Amet minim mollit non deserunt ullamco est sit aliqua dolor do amet sint.</p></div>
<div class="ref-card faded" style="left:1078px"><div class="photo" role="img" aria-label="Foto eines hellen Innenraums" style="background:linear-gradient(135deg,#f0eeea,#d6cfc4)"></div><h3>Nordlicht</h3><p>Amet minim mollit non deserunt ullamco est sit aliqua dolor do amet sint.</p></div>

<div class="arrow-btn" style="left:932px"><svg width="37" height="35"><path d="M27 17.5H10M16 11.5l-6 6 6 6" stroke="#b8c0c6" stroke-width="1.6" fill="none"/></svg></div>
<div class="arrow-btn active" style="left:986px"><svg width="37" height="35"><path d="M10 17.5h17M21 11.5l6 6-6 6" stroke="#1b6dbb" stroke-width="1.6" fill="none"/></svg></div>

<section class="contact">
  <h2>Kontakt</h2>
  <p class="intro">Sie können uns jederzeit kontaktieren. Wir werden so schnell wie möglich auf Sie zurückkommen!</p>
</section>
<div class="info" style="top:4730px"><b>Address</b><span>48 Birkenweg, Talheim, Nordland 40218</span></div>
<div class="info" style="top:4810px"><b>Phone</b><span>(555) 380-4416</span></div>
<div class="info" style="top:4888px"><b>Email</b><span>kontakt@lumivelde.example</span></div>
<div class="field" style="top:4584px;height:60px">Name</div>
<div class="field" style="top:4666px;height:60px">Email</div>
<div class="field" style="top:4748px;height:122px;padding-top:14px">Message</div>
<div class="submit">EINREICHEN</div>

<footer class="site-footer">
  <div class="links"><a style="left:222px">AGB</a><a style="left:274px">Impressum</a><a style="left:372px">Datenschutz</a></div>
  <div class="go">Los geht's! —</div>
  <div class="go-btn">Jetzt Anrufen</div>
  <div class="copyright">© 2021 All Rights Reserved</div>
</footer>

</body>
</html>
```